Lumen Harvest Fellowship Direct Mail Postcard

We are launching a new church in Olathe Kansas (Kansas City suburb). People here are well educated and pretty affluent. There are many young families which is our mail target demo. We need a 6 inch by 11 inch postcard that will be for a mass mailer that will coincide with our launch. The goal is simply to get people to come to the church launch which is September 18th. We think the theme should be "What in Heaven are you here for?" or "God is not Mad at you..No Matter What?" or "The truth is...you matter." It needs to include a map to our church which is inside Copperleaf Ridge Middle School: 18350 W 94th St, Olathe, KS 66062. Service is at 10:00 am, Safe childcare is provided from infants up to 12 year olds. There should be some space for us to put in some messaging and bullets. Possibly include a few pictures of happy families and people worshiping. I’ve attached our Logo, but we actually need to flip the colors so that the blue arrow is on top and pointing down, and the gray arrow is pointing up.

Target Market(s)

Young Families

Industry/Entity Type

Church

Requirements
Must have
• Post Card should be front and back full color
• Our website clearly shown on the back: LumenHarvestFellowship.com
• There should be a small map on the back with our location.
• It should say our service starts at 10:00 and that we our first service is Sept 18th
• The message or images on the front are there primarily to get people to turn the card over. UPDATE: We like the idea "What in Heaven are you here for?" on the front the best, followed by "God is NOT Mad at you..." (front) "no matter what" (back) second, and then "The truth is.." (front) "You matter" back third.
• Only 1 of the themes should be used at a time. So for example, the front should say, "What In Heaven are you here for?" or "God is not mad at you..." but not both.
• We like clean, modern looks. Don't put the logo on the front.
Nice to have
• Some stock photos of families or people worshipping (contemporary charismatic church)
• I attached some examples of cards that worked well for other churches. Please check them out.
Should not have
• The words "Grand Opening"

```html
<!DOCTYPE html>
<html lang="en">
<head>
<meta charset="utf-8">
<title>Lumen Harvest Fellowship – Launch Postcard</title>
<link rel="stylesheet" href="https://fonts.googleapis.com/css2?family=Cormorant+Garamond:wght@500;600&family=Oswald:wght@400;500&family=Source+Sans+3:wght@300;400;600;700;800&display=swap">
<style>
  :root {
    --stage: #a6aa9e;
    --cream: #f3f0e8;
    --paper: #f6f5f1;
    --ink: #1d1d22;
    --brand-blue: #1b2fe0;
    --rule-blue: #3048c8;
    --grey-line: #bdbdbd;
  }
  * { box-sizing: border-box; margin: 0; padding: 0; }
  html, body { width: 1200px; height: 1199px; overflow: hidden; }
  body { background: var(--stage); position: relative; font-family: "Source Sans 3", sans-serif; color: var(--ink); }

  .card { position: absolute; top: 145px; width: 508px; height: 912px; overflow: hidden; box-shadow: 0 6px 24px rgba(0,0,0,.35); }

  /* FRONT */
  .card--front {
    left: 78px;
    background:
      radial-gradient(ellipse 120px 240px at 440px 530px, rgba(235,170,60,.9), rgba(160,100,25,.4) 45%, transparent 80%),
      radial-gradient(ellipse 90px 200px at 330px 530px, rgba(200,140,40,.55), transparent 80%),
      linear-gradient(90deg, #0a0a10 0%, #15131a 55%, #1e1a16 78%, #0e0d0c 100%);
  }
  .front__light {
    position: absolute; left: 343px; top: 0; width: 61px; height: 912px;
    background: linear-gradient(180deg, #1f4fae 0%, #5f9ede 14%, #cfe4f6 35%, #ffffff 52%, #d9e9f7 75%, #b9d6f0 100%);
  }
  .front__kicker, .front__footer {
    position: absolute; right: 218px; text-align: right; white-space: nowrap;
    font-family: "Cormorant Garamond", serif; font-weight: 600; font-size: 13.5px;
    letter-spacing: 2.9px; line-height: 15px; color: var(--cream); text-transform: uppercase;
  }
  .front__kicker { top: 124px; }
  .front__footer { top: 824px; }
  .headline { font-family: "Cormorant Garamond", serif; font-weight: 600; color: var(--cream); position: absolute; inset: 0; line-height: 1; }
  .headline span { position: absolute; white-space: nowrap; }
  .h-what { left: 45px; top: 271px; font-size: 72px; }
  .h-heaven { left: 84px; top: 341px; font-size: 80px; }
  .h-in { left: 169px; top: 345px; font-size: 28px; }
  .h-are { left: 109px; top: 417px; font-size: 32px; }
  .h-here { left: 57px; top: 442px; font-size: 52px; }
  .h-q { left: 219px; top: 423px; font-size: 76px; }

  /* BACK */
  .card--back { left: 619px; background: var(--paper); }
  .photos { display: flex; height: 105px; }
  .photos__item { flex: 1; }
  .photo-1 { background: linear-gradient(135deg, #c9b08e, #6b5644 70%, #3a2e28); }
  .photo-2 { background: linear-gradient(135deg, #8a8f7a, #c9a58f 55%, #6f6a74); }
  .photo-3 { background: linear-gradient(135deg, #d9d3c6, #6c5a4c 60%, #3c4a6a); }

  .center { position: absolute; left: 0; width: 100%; text-align: center; }
  .eyebrow { top: 131px; font-family: "Oswald", sans-serif; font-weight: 500; font-size: 16px; }
  .brand { top: 156px; font-family: "Oswald", sans-serif; font-weight: 500; font-size: 33px; color: var(--brand-blue); letter-spacing: -.2px; display: flex; justify-content: center; align-items: center; gap: 10px; }
  .brand__mark { width: 20px; height: 20px; background: var(--brand-blue); }
  .tagline { top: 193px; font-weight: 300; font-size: 19px; }
  .rule { position: absolute; left: 42px; width: 415px; top: 231px; height: 2px; background: var(--rule-blue); }
  .slash { color: var(--brand-blue); font-style: italic; font-weight: 400; }
  .opens { top: 244px; font-size: 27px; font-weight: 400; letter-spacing: 1.2px; }
  .opens b { font-weight: 800; letter-spacing: 2px; }
  .opens small, .starts small { font-size: 17px; font-weight: 800; }
  .starts { top: 281px; font-size: 19px; font-weight: 800; }
  .starts .time { font-size: 25px; }
  .motto { top: 323px; font-size: 14.5px; font-weight: 800; line-height: 17px; }
  .invite { top: 366px; font-size: 14.5px; font-weight: 700; }
  .body-copy { position: absolute; left: 42px; width: 420px; top: 397px; font-size: 12.5px; line-height: 16px; }
  .findings-title { top: 463px; font-size: 12.5px; font-weight: 700; }
  .findings-title::before, .findings-title::after { content: ""; position: absolute; top: 9px; width: 64px; height: 1px; background: #444; }
  .findings-title::before { left: 42px; } .findings-title::after { right: 51px; }
  .features { position: absolute; top: 488px; left: 43px; display: grid; grid-template-columns: 182px 240px; row-gap: 5px; list-style: none; font-size: 12.5px; font-weight: 700; }
  .features li::before { content: "✓"; color: var(--brand-blue); margin-right: 8px; }
  .childcare { top: 542px; font-size: 13.5px; font-weight: 800; }
  .childcare .blue { color: var(--brand-blue); }
  .childcare svg { vertical-align: -1px; margin-right: 5px; }

  .message-area { position: absolute; left: 0; top: 573px; width: 261px; height: 339px; background: #fff; border-right: 2px solid var(--grey-line); }
  .map { position: absolute; left: 274px; top: 573px; width: 200px; height: 137px; background: linear-gradient(180deg, #eef0f6, #dfe3ee); border: 2px solid var(--rule-blue); }
  .venue { position: absolute; left: 276px; top: 720px; font-size: 12px; line-height: 14px; }
  .venue strong { font-weight: 700; display: block; }
  .site { position: absolute; left: 275px; top: 759px; font-size: 15px; font-weight: 700; color: var(--brand-blue); }
  .stamp { position: absolute; left: 358px; top: 802px; width: 115px; height: 76px; border: 1px dashed #888; }
</style>
</head>
<body>

<section class="card card--front" aria-label="Postcard front">
  <div class="front__light" role="img" aria-label="Bright strip of blue sky and clouds breaking through darkness"></div>
  <p class="front__kicker">Based on our Lord<br>incredible true story.</p>
  <h1 class="headline">
    <span class="h-what">What</span>
    <span class="h-heaven">Heaven</span>
    <span class="h-in">in</span>
    <span class="h-are">are you</span>
    <span class="h-here">here for</span>
    <span class="h-q">?</span>
  </h1>
  <p class="front__footer">See the<br>mistery unlocks.</p>
</section>

<section class="card card--back" aria-label="Postcard back">
  <div class="photos">
    <div class="photos__item photo-1" role="img" aria-label="Photo of a smiling young couple"></div>
    <div class="photos__item photo-2" role="img" aria-label="Photo of two happy sisters"></div>
    <div class="photos__item photo-3" role="img" aria-label="Photo of a family with their daughter"></div>
  </div>

  <p class="center eyebrow">FIND THE ANSWERS AT</p>
  <p class="center brand"><span class="brand__mark"></span>LUMEN HARVEST FELLOWSHIP</p>
  <p class="center tagline">Love · Wisdom · Power</p>
  <div class="rule"></div>

  <p class="center opens"><span class="slash">//</span> OPENS AT <b>SEPTEMBER18</b><small>TH</small></p>
  <p class="center starts"><span class="slash">//</span> SERVICE STARTS AT <span class="time">10:00</span><small>AM</small></p>
  <p class="center motto">DON’T JUST SURVIVE, LIVE. LIVE TO THE FULLEST OF YOUR<br>HABILITIES, SHOUT TO THE HEAVENS WITH YOUR FULL VOICE.</p>
  <p class="center invite">Bring your family and Join us on our first session.</p>
  <p class="body-copy">At Lumen Harvest Fellowship, we provide all the counseling you need to find a new path in life. We work to maintain the ultimate values of life, like love, wisdom and the commitment to help others.</p>

  <p class="center findings-title">At Lumen Harvest Fellowship, you will find:</p>
  <ul class="features">
    <li>A friendly enviroment</li>
    <li>Enlightening messages and counseling</li>
    <li>Dinamic Worship Experience</li>
    <li>A safe enviroment for your children</li>
  </ul>
  <p class="center childcare">
    <svg width="13" height="12" viewBox="0 0 24 22" aria-hidden="true"><path fill="#1b2fe0" d="M12 21 2.5 11.6A5.8 5.8 0 0 1 12 3.7a5.8 5.8 0 0 1 9.5 7.9z"/></svg><span class="blue">SAFE CHILDCARE</span> FROM INFANTS UP TO 12 YEAR OLDS
  </p>

  <div class="message-area" aria-label="Space for personal message"></div>
  <div class="map" role="img" aria-label="Street map showing the church location at Copperleaf Ridge Middle School"></div>
  <p class="venue"><strong>COPPERLEAF RIDGE MIDDLE SCHOOL</strong>18350 W 94th St, Olathe, KS 66062</p>
  <p class="site">LumenHarvestFellowship.com</p>
  <div class="stamp" aria-label="Postage area"></div>
</section>

</body>
</html>
```